CASH PAYMENT DISCOUNT NOTICE POSTED IN CASH REGISTER AREA

LOOKING TO MAKE A FLYER OR A POSTED NOTICE FOR CUSTOMERS PAYING FOR OVER-THE-COUNTER MERCHANDISE AND WHO PAY BY CASH METHOD TO GET A 4% CASH DISCOUNT.
PRESCRIPTIONS ARE EXCLUDED FROM THIS CASH DISCOUNT.

Target Market(s)

RETAIL CUSTOMERS

Industry/Entity Type

RETAIL PHARMACY

Colors
0054AA
0677BA
7BADD7
CADEEF
E8F1F8
EB3D1F
EC4F4E
F09395
F8D3D4
FCEDEE

Requirements
Must have
• LOGO COLORS
Nice to have
• EYE CATCHING

```html
<!DOCTYPE html>
<html lang="en">
<head>
<meta charset="utf-8">
<title>Cash Discount Notice</title>
<link rel="stylesheet" href="https://fonts.googleapis.com/css2?family=Montserrat:wght@600;700;800&display=swap">
<style>
  :root {
    --backdrop: #e5e5e5;
    --card: #ffffff;
    --brand-blue: #344b9c;
    --brand-red: #b5181b;
    --ink: #1a1a1a;
  }
  html, body {
    margin: 0;
    padding: 0;
    width: 1200px;
    height: 1200px;
    overflow: hidden;
    background: var(--backdrop);
    font-family: "Montserrat", Arial, sans-serif;
  }
  .notice {
    position: absolute;
    left: 68px;
    top: 287px;
    width: 1065px;
    height: 613px;
    background: var(--card);
    overflow: hidden;
  }
  .notice__swooshes {
    position: absolute;
    inset: 0;
    width: 100%;
    height: 100%;
  }
  .swoosh--blue { fill: var(--brand-blue); }
  .swoosh--red { fill: var(--brand-red); }

  .brand {
    position: absolute;
    left: 0;
    right: 0;
    top: 92px;
    display: flex;
    justify-content: center;
    align-items: center;
    gap: 18px;
  }
  .brand__mark {
    width: 44px;
    height: 44px;
    background: var(--brand-blue);
  }
  .brand__name {
    font-weight: 700;
    font-size: 50px;
    color: var(--brand-blue);
    letter-spacing: 0.5px;
  }

  .headline {
    position: absolute;
    left: 0;
    right: 0;
    top: 235px;
    margin: 0;
    text-align: center;
    font-weight: 800;
    font-size: 72px;
    line-height: 1;
    color: var(--brand-blue);
    letter-spacing: 1px;
    transform: translateX(-10px);
  }
  .offer {
    position: absolute;
    left: 0;
    right: 0;
    top: 324px;
    margin: 0;
    text-align: center;
    font-weight: 700;
    font-size: 30px;
    line-height: 41px;
    color: var(--ink);
    transform: translateX(12px);
  }
  .offer__highlight { color: var(--brand-red); }
  .exclusion {
    position: absolute;
    left: 0;
    right: 0;
    top: 514px;
    margin: 0;
    text-align: center;
    font-weight: 700;
    font-size: 22px;
    line-height: 30px;
    color: var(--ink);
    letter-spacing: 0.3px;
    transform: translateX(12px);
  }
</style>
</head>
<body>
  <section class="notice">
    <svg class="notice__swooshes" viewBox="0 0 1420 818" preserveAspectRatio="none" aria-hidden="true">
      <path class="swoosh--blue" d="M0,0 H575 C380,40 150,170 0,300 Z"/>
      <path class="swoosh--red" d="M0,315 C160,175 400,40 610,0 H660 C420,40 170,200 0,410 Z"/>
      <path class="swoosh--red" d="M1420,500 C1280,680 1080,780 860,818 H905 C1090,785 1270,700 1420,578 Z"/>
      <path class="swoosh--blue" d="M1420,590 C1260,715 1090,790 915,818 H1420 Z"/>
    </svg>

    <div class="brand">
      <span class="brand__mark"></span>
      <span class="brand__name">Halden Pharmacy</span>
    </div>

    <h1 class="headline">CASH DISCOUNT</h1>

    <p class="offer">
      AS AN INCENTIVE FOR CUSTOMERS, WE NOW<br>
      PROVIDE A DISCOUNT TO PAY WITH CASH BY GIVING<br>
      A <span class="offer__highlight">4% IMMEDIATE DISCOUNT</span> ON THE<br>
      SERVICE CHARGE.
    </p>

    <p class="exclusion">
      PRESCRIPTIONS ARE EXCLUDED FROM<br>
      THIS CASH DISCOUNT
    </p>
  </section>
</body>
</html>
```